Mobile Fitness snd Therapy Business Card Design

I need a business card designed for my mobile fitness and therapy business.

Please view the images that I have uploaded. I like the simplicity of the design that I have attached. I adapted it with my information

Target Market(s)

Those seeking personal training, injury rehabilitation or massage therapy.

Industry/Entity Type

Business

Contact Information for Business Card

Dylan Marwick - MSc, CAT(C), RMT, CSCS, Pn2
e-mail: dylan@vantrelo.com
website: www.vantrelo.com
instagram: @dylan_marwick

Font styles to use
Sans Serif

Colors
3176b5
0355a3

Requirements
Must have
• "Contact us to receive a FREE assessment"
• Services offered:
• Personal Training
• Golf Fitness
• Injury Rehab
• Massage Therapy
• Yoga
Nice to have
• Consistent colours with brand
• - Dark Blue: #232837
• - Blue: #5096f0
• Consistent look/feel with the website: www.vantrelo.com

```html
<!DOCTYPE html>
<html lang="en">
<head>
<meta charset="utf-8">
<title>Vantrelo Business Card</title>
<link rel="stylesheet" href="https://fonts.googleapis.com/css2?family=Montserrat:wght@600;700&family=Open+Sans:wght@400;600&display=swap">
<style>
  :root {
    --backdrop: #e6e7ea;
    --card: #232837;
    --ink: #ffffff;
    --accent: #5096f0;
    --brand-blue: #3176b5;
    --rule: #c9ccd3;
  }
  * { margin: 0; padding: 0; box-sizing: border-box; }
  html, body {
    width: 1200px; height: 1000px; overflow: hidden;
    background: var(--backdrop);
  }
  .canvas { position: relative; width: 1200px; height: 1000px; }
  .card {
    position: absolute; left: 266px; width: 666px; height: 397px;
    background: var(--card); color: var(--ink);
    box-shadow: 0 6px 18px rgba(0,0,0,.25);
  }
  .card--front { top: 74px; }
  .card--back { top: 533px; }

  .brand { position: absolute; left: 0; right: 0; text-align: center; }
  .brand__name {
    font-family: "Montserrat", sans-serif; font-weight: 600;
    letter-spacing: 4px; line-height: 1; color: var(--ink);
  }
  .brand__tagline {
    font-family: "Montserrat", sans-serif; font-weight: 700;
    letter-spacing: 2.6px; line-height: 1; color: var(--ink);
  }
  .card--front .brand { top: 52px; }
  .card--front .brand__name { font-size: 52px; }
  .card--front .brand__tagline { font-size: 16px; margin-top: 10px; }
  .card--back .brand { top: 168px; }
  .card--back .brand__name { font-size: 56px; }
  .card--back .brand__tagline { font-size: 18px; margin-top: 12px; }

  .edge-bar {
    position: absolute; top: 170px; width: 7px; height: 140px;
    background: var(--ink);
  }
  .edge-bar--left { left: 0; }
  .edge-bar--right { right: 0; }

  .person { position: absolute; left: 80px; top: 177px; font-family: "Open Sans", sans-serif; }
  .person__name {
    font-family: "Montserrat", sans-serif; font-weight: 600;
    font-size: 21px; letter-spacing: .3px; line-height: 1;
  }
  .person__credentials { font-size: 14px; color: var(--accent); margin-top: 8px; }

  .contact-list { list-style: none; position: absolute; left: 79px; top: 242px; font-family: "Open Sans", sans-serif; font-size: 17px; }
  .contact-list li { display: flex; align-items: center; height: 24px; }
  .contact-list li:first-child { margin-bottom: 4px; }
  .contact-list svg { width: 16px; height: 16px; margin-right: 7px; flex: none; }

  .divider { position: absolute; left: 332px; top: 178px; width: 2px; height: 139px; background: var(--rule); }

  .services { list-style: none; position: absolute; left: 382px; top: 172px; font-family: "Open Sans", sans-serif; font-size: 18px; }
  .services li { display: flex; align-items: center; height: 30.5px; }
  .services li::before {
    content: ""; width: 9px; height: 9px; margin-right: 10px;
    background: var(--accent);
  }

  .offer {
    position: absolute; left: 0; right: 0; top: 341px; text-align: center;
    font-family: "Open Sans", sans-serif; font-size: 17px;
  }
</style>
</head>
<body>
<main class="canvas">
  <section class="card card--front" aria-label="Business card front">
    <div class="brand">
      <div class="brand__name">VANTRELO</div>
      <div class="brand__tagline">NUTRITION - FITNESS - HEALTH</div>
    </div>

    <span class="edge-bar edge-bar--left"></span>
    <span class="edge-bar edge-bar--right"></span>

    <div class="person">
      <div class="person__name">DYLAN MARWICK</div>
      <div class="person__credentials">MSc, CAT(C), RMT, CSCS, Pn2</div>
    </div>

    <ul class="contact-list">
      <li>
        <svg viewBox="0 0 16 16" aria-hidden="true"><rect x="2" y="2" width="12" height="12" fill="#ffffff"/></svg>
        @dylan_marwick
      </li>
      <li>
        <svg viewBox="0 0 16 16" aria-hidden="true"><rect x="1" y="3" width="14" height="10" fill="#ffffff"/><path d="M1.5 3.5 8 9l6.5-5.5" fill="none" stroke="#232837" stroke-width="1.4"/></svg>
        dylan@vantrelo.com
      </li>
      <li>
        <svg viewBox="0 0 16 16" aria-hidden="true"><circle cx="8" cy="8" r="6.3" fill="none" stroke="#ffffff" stroke-width="1.5"/><ellipse cx="8" cy="8" rx="2.6" ry="6.3" fill="none" stroke="#ffffff" stroke-width="1.2"/><path d="M1.8 8h12.4" stroke="#ffffff" stroke-width="1.2"/></svg>
        www.vantrelo.com
      </li>
    </ul>

    <span class="divider"></span>

    <ul class="services">
      <li>Personal Training</li>
      <li>Golf Fitness</li>
      <li>Injury Rehab</li>
      <li>Massage Therapy</li>
      <li>Yoga</li>
    </ul>

    <p class="offer">Contact us to receive a FREE assessment</p>
  </section>

  <section class="card card--back" aria-label="Business card back">
    <div class="brand">
      <div class="brand__name">VANTRELO</div>
      <div class="brand__tagline">NUTRITION - FITNESS - HEALTH</div>
    </div>
  </section>
</main>
</body>
</html>
```